Young Accounting firm needing a captivating business card

We need a business card design that forces the person to look at the card because its either gold foil, plastic, or lettering pop up etc. We already have a logo with a specific gold color and we need to make it pop. We are an accounting firm. I need the words" accounting, payroll, licenses, audits, taxes" somewhere on the business card so as to describe what we do- preferably on the side where the logo is at.

Industry/Entity Type

Accounting

Contact Information for Business Card

Address 48207 7th Ave N Ste 305, Federal Way, WA 98117
Business Phone (360)555-0147
Fax (360)555-0193
Office Cell Phone (360)555-0162

Font styles to use
Serif

Colors
85abd2

Requirements
Must have
• It should state
• "Accounting" "Taxes" "Audits" "Licenses" "Payroll"
Nice to have
• Matte with gold foil, different textures, With Either a textured ivory background or gray blue slate background
Should not have
• colorful colors

```html
<!DOCTYPE html>
<html lang="en">
<head>
<meta charset="utf-8">
<title>NVLedgerwise Business Card</title>
<link href="https://fonts.googleapis.com/css2?family=Tinos:wght@400;700&display=swap" rel="stylesheet">
<style>
  :root {
    --backdrop: #eff1f0;
    --card-white: #ffffff;
    --slate: #28282c;
    --gold: #b8972f;
    --gold-light: #d6ad3c;
    --wine: #7a1e14;
    --blue: #3a6fb5;
    --green: #2e6b4a;
    --olive: #545a3a;
    --ink: #1d1d1f;
  }
  * { margin: 0; padding: 0; box-sizing: border-box; }
  html, body {
    width: 1200px; height: 1200px; overflow: hidden;
    background: var(--backdrop);
    font-family: "Tinos", "Times New Roman", serif;
  }
  .canvas { position: relative; width: 1200px; height: 1200px; }
  .business-card {
    position: absolute; left: 116px; top: 314px;
    width: 984px; height: 562px;
    background: var(--card-white);
    box-shadow: 4px 6px 10px rgba(0,0,0,0.35);
  }
  .card-shapes { position: absolute; inset: 0; width: 984px; height: 562px; overflow: visible; }
  .brand-mark {
    position: absolute; left: 186px; top: 140px;
    width: 110px; height: 110px; background: var(--gold);
  }
  .brand-name {
    position: absolute; left: 0; width: 482px; top: 262px;
    text-align: center; color: var(--gold);
    font-size: 62px; font-weight: 400; line-height: 1;
  }
  .contact-item {
    position: absolute; display: flex; align-items: center; gap: 8px;
    font-size: 17px; color: var(--ink); line-height: 1;
  }
  .contact-item svg { width: 22px; height: 22px; fill: var(--gold); flex: none; }
  .service-label {
    position: absolute; top: 447px; width: 190px;
    text-align: center; font-size: 29px; line-height: 1;
  }
  .on-gold { color: var(--wine); }
  .on-dark { color: var(--gold-light); }
</style>
</head>
<body>
<div class="canvas">
  <div class="business-card">
    <svg class="card-shapes" viewBox="0 0 984 562" aria-hidden="true">
      <polygon points="436,0 450,0 612,562 596,562" fill="#9a9a9a"/>
      <polygon points="0,0 424,0 596,562 0,562" fill="var(--slate)"/>
      <g class="service-shadows" fill="#1a1a1a" opacity="0.75">
        <polygon points="20,442 210,442 223,494 33,494"/>
        <polygon points="210,442 400,442 413,494 223,494"/>
        <polygon points="397,442 587,442 600,494 410,494"/>
        <polygon points="585,442 775,442 788,494 598,494"/>
        <polygon points="775,442 970,442 970,494 788,494"/>
      </g>
      <polygon points="14,436 204,436 217,488 27,488" fill="var(--wine)"/>
      <polygon points="204,436 394,436 407,488 217,488" fill="var(--gold)"/>
      <polygon points="391,436 581,436 594,488 404,488" fill="var(--blue)"/>
      <polygon points="579,436 769,436 782,488 592,488" fill="var(--green)"/>
      <polygon points="769,436 964,436 958,488 782,488" fill="var(--olive)"/>
    </svg>

    <div class="brand-mark"></div>
    <div class="brand-name">NVLedgerwise</div>

    <div class="contact-item" style="left:494px; top:125px;">
      <svg viewBox="0 0 24 24"><path d="M12 3 2 12h3v9h5v-6h4v6h5v-9h3z"/></svg>
      <span>48207 7th Ave N Ste 305, Federal Way, WA 98117</span>
    </div>
    <div class="contact-item" style="left:509px; top:171px;">
      <svg viewBox="0 0 24 24"><path d="M2 5h20v14H2zm1.5 1.5v.3L12 13l8.5-6.2v-.3zm0 2.2v8.8h17V8.7L12 14.9z"/></svg>
      <span>Email</span>
    </div>
    <div class="contact-item" style="left:529px; top:216px;">
      <svg viewBox="0 0 24 24"><path d="M6.6 10.8a15 15 0 0 0 6.6 6.6l2.2-2.2c.3-.3.7-.4 1-.2 1.1.4 2.3.6 3.6.6.6 0 1 .4 1 1V20c0 .6-.4 1-1 1A17 17 0 0 1 3 4c0-.6.4-1 1-1h3.5c.6 0 1 .4 1 1 0 1.3.2 2.5.6 3.6.1.3 0 .7-.2 1z"/></svg>
      <span>(360)555-0147</span>
    </div>
    <div class="contact-item" style="left:543px; top:263px;">
      <svg viewBox="0 0 24 24"><path d="M6 2h12v5H6zM3 8h18a1 1 0 0 1 1 1v7h-4v-3H6v3H2V9a1 1 0 0 1 1-1zm3 6h12v8H6z"/></svg>
      <span>(360)555-0193</span>
    </div>
    <div class="contact-item" style="left:557px; top:311px;">
      <svg viewBox="0 0 24 24"><path d="M7 1h10a1 1 0 0 1 1 1v20a1 1 0 0 1-1 1H7a1 1 0 0 1-1-1V2a1 1 0 0 1 1-1zm1 3v15h8V4zm4 16.5a1 1 0 1 0 0 .1z"/></svg>
      <span>(360)555-0162</span>
    </div>

    <div class="service-label on-dark" style="left:25px;">Accounting</div>
    <div class="service-label on-gold" style="left:210px;">Payroll</div>
    <div class="service-label on-dark" style="left:397px;">Licenses</div>
    <div class="service-label on-gold" style="left:585px;">Audits</div>
    <div class="service-label on-dark" style="left:772px;">Taxes</div>
  </div>
</div>
</body>
</html>
```